Wordpress website design for Tavi Linkway-Africa

We need a website for a new consultancy and digital marketplace in Kenya called 'Tavi Linkway - Africa'. Please refer to the the attached document [Tavi Linkway Africa website brief] and contact me anytime.

Bests,
Philippa

Deadline extended to allow for additional revisions and refinements, ensuring that final designs align closely with project objectives and quality standards. This extra time will help incorporate valuable feedback and ensure the final output meets our high expectations.

```html
<!DOCTYPE html>
<html lang="en">
<head>
<meta charset="UTF-8">
<title>Tavi Linkway Africa</title>
<link href="https://fonts.googleapis.com/css2?family=Poppins:wght@400;500;600;700;800&display=swap" rel="stylesheet">
<style>
:root{
  --yellow:#f7b500;
  --ink:#111111;
  --text:#3a3a3a;
  --muted:#6b6b6b;
  --paper:#ffffff;
  --mist:#f1f1f1;
  --cloud:#e6e6e6;
  --night:#1b1b1b;
  --line:#dcdcdc;
}
*{box-sizing:border-box;margin:0;padding:0}
html,body{width:1200px;height:3236px;overflow:hidden}
body{font-family:"Poppins",sans-serif;color:var(--text);background:var(--paper);position:relative}
a{color:inherit;text-decoration:none}
.abs{position:absolute}

/* nav */
.nav{left:0;top:0;width:1200px;height:62px;display:flex;align-items:center;padding:0 40px;justify-content:space-between;z-index:5}
.brand{font-weight:800;font-size:22px;color:var(--ink);letter-spacing:.5px}
.nav-links{display:flex;gap:22px;font-size:13px;color:var(--ink);align-items:center;margin-left:auto;margin-right:22px}
.btn-login{background:var(--yellow);color:var(--ink);font-weight:600;font-size:12px;padding:7px 22px;border-radius:20px}

/* hero */
.hero-bg{left:0;top:0;width:1200px;height:720px}
.hero-copy{left:40px;top:168px;width:560px;z-index:2}
.hero-title{font-size:41px;line-height:1.12;font-weight:800;color:var(--ink)}
.hero-text{font-size:13px;line-height:1.6;margin-top:16px;width:470px;color:var(--text)}
.hero-actions{display:flex;gap:14px;margin-top:24px}
.btn{display:inline-block;font-size:13px;font-weight:600;padding:10px 22px;border-radius:24px}
.btn-yellow{background:var(--yellow);color:var(--ink)}
.btn-outline{border:1.5px solid var(--ink);color:var(--ink)}
.hero-art{left:640px;top:70px;width:460px;height:500px;border-radius:24px;background:linear-gradient(160deg,#f2f2f2 0%,#e4e4e4 55%,#f7c542 100%)}

/* section titles */
.sec-title{left:0;width:1200px;text-align:center;font-size:40px;font-weight:800;color:var(--ink);line-height:1.2}
.sec-sub{left:0;width:1200px;text-align:center;font-size:13px;color:var(--muted)}

/* services */
.services{left:88px;top:764px;width:1032px;display:flex;gap:16px}
.service-card{flex:1;border:1px solid var(--line);background:var(--paper);height:214px}
.service-img{height:158px}
.service-name{font-size:15px;font-weight:700;color:var(--ink);text-align:center;padding-top:16px}

/* about */
.about-art{left:160px;top:1060px;width:380px;height:380px;border-radius:12px;background:linear-gradient(160deg,#f4f4f4,#dedede 65%,#f5d37a)}
.about-copy{left:590px;top:1100px;width:540px}
.about-title{font-size:40px;font-weight:800;color:var(--ink);margin-bottom:10px;line-height:1.2}
.about-copy p{font-size:13px;line-height:1.6;margin-bottom:10px}

/* marketplace */
.market-band{left:0;top:1460px;width:1200px;height:680px}
.tabs{left:0;top:1798px;width:1200px;display:flex;justify-content:center;gap:20px;font-size:12px;color:var(--muted)}
.tabs .on{color:var(--yellow);font-weight:600}
.products{left:90px;top:1830px;width:1024px;display:flex;gap:16px}
.product{flex:1;background:var(--paper);border-radius:6px;box-shadow:0 4px 14px rgba(0,0,0,.08);height:262px}
.product-img{height:100px;border-radius:6px 6px 0 0}
.product-body{padding:8px 12px}
.product-head{display:flex;justify-content:space-between;align-items:baseline}
.product-name{font-size:13px;font-weight:700;color:var(--ink)}
.price{font-size:15px;font-weight:700;color:var(--ink)}
.price small{font-size:9px;font-weight:400;color:var(--muted)}
.product-desc{font-size:10px;line-height:1.45;margin-top:4px;height:44px;overflow:hidden}
.stars{display:flex;gap:2px;align-items:center;margin-top:4px;font-size:10px;color:var(--muted)}
.stars svg{width:11px;height:11px;fill:var(--yellow)}
.btn-shop{display:block;text-align:center;background:var(--ink);color:#fff;font-size:11px;font-weight:600;border-radius:16px;padding:5px 0;margin-top:8px}
.btn-save{display:block;text-align:center;border:1px solid var(--line);font-size:10px;border-radius:16px;padding:4px 0;margin-top:6px;color:var(--ink)}

/* why */
.why-title span{color:var(--yellow)}
.reasons{left:190px;top:2362px;width:820px;display:flex;justify-content:space-between}
.reason{width:240px;text-align:center}
.reason-icon{width:78px;height:78px;border-radius:50%;background:var(--yellow);margin:0 auto 14px;display:flex;align-items:center;justify-content:center}
.reason-icon.dark{background:var(--ink)}
.reason-icon svg{width:36px;height:36px}
.reason h3{font-size:16px;font-weight:700;color:var(--ink)}
.reason p{font-size:12px;line-height:1.5;margin-top:4px}

/* footer */
.footer-bg{left:0;top:2760px;width:1200px;height:476px}
.cta{left:120px;top:2620px;width:960px;height:230px;background:var(--yellow);border-radius:115px;padding:56px 90px;display:flex;justify-content:space-between;align-items:center;z-index:2}
.cta h2{font-size:33px;line-height:1.15;font-weight:800;color:var(--ink);width:520px}
.cta p{font-size:12px;margin-top:10px;color:var(--ink)}
.btn-dark{background:var(--ink);color:#fff;font-size:13px;font-weight:600;padding:10px 36px;border-radius:22px;white-space:nowrap}
.f-brand{left:120px;top:2995px;font-size:30px;font-weight:800;color:#fff}
.f-col{top:2950px;color:#d6d6d6;font-size:12.5px}
.f-col h4{font-size:17px;font-weight:700;color:#fff;margin-bottom:8px}
.f-col h4 span{color:var(--yellow)}
.f-col li{list-style:none;line-height:1.65}
.f-col p{line-height:1.55;width:230px}
.signup{display:flex;background:#fff;border-radius:20px;width:240px;height:36px;margin-top:14px;padding:3px}
.signup span{flex:1;font-size:11px;color:var(--muted);padding:8px 12px}
.signup b{width:30px;height:30px;border-radius:50%;background:var(--yellow)}
.socials{left:960px;top:3015px;display:flex;gap:14px}
.socials i{width:22px;height:22px;border-radius:50%;background:#3a3a3a;display:block}
.copyright{left:0;top:3196px;width:1200px;text-align:center;font-size:11px;color:#bdbdbd}
.to-top{left:1110px;top:3178px;width:36px;height:36px;border-radius:50%;background:var(--yellow)}
</style>
</head>
<body>

<svg class="abs hero-bg" viewBox="0 0 1200 720" aria-hidden="true">
  <path d="M0 600 C200 570 360 660 560 640 C780 620 880 570 1200 610 L1200 720 L0 720Z" fill="var(--mist)"/>
</svg>

<header class="abs nav">
  <div class="brand">Tavi Linkway</div>
  <nav class="nav-links">
    <a>Home</a><a>Services</a><a>Digital Marketplace</a><a>About Us</a><a>Blog</a><a>Contact</a>
  </nav>
  <a class="btn-login">Log in</a>
</header>

<div class="abs hero-art" role="img" aria-label="Hero illustration: astronaut riding a shopping cart with light bulbs"></div>

<section class="abs hero-copy">
  <h1 class="hero-title">Empowering Innovations &amp; Digital Transformation Across Africa</h1>
  <p class="hero-text">Transform your vision into reality with Tavi Linkway Africa. We offer expert consultancy and a dynamic digital marketplace tailored to support Africa's growth through cutting-edge solutions and tools.</p>
  <div class="hero-actions">
    <a class="btn btn-yellow">Explore Our Services</a>
    <a class="btn btn-outline">Visit the Marketplace</a>
  </div>
</section>

<h2 class="abs sec-title" style="top:664px">Our Services</h2>
<p class="abs sec-sub" style="top:718px">Transforming Your Operations with Our Expertise</p>

<section class="abs services">
  <div class="service-card"><div class="service-img" role="img" aria-label="Digital strategy illustration" style="background:linear-gradient(135deg,#1d2a4a,#3b5d9a)"></div><div class="service-name">Digital Strategy</div></div>
  <div class="service-card"><div class="service-img" role="img" aria-label="Technical expertise illustration" style="background:linear-gradient(135deg,#e2573c,#2b3566)"></div><div class="service-name">Technical Expertise</div></div>
  <div class="service-card"><div class="service-img" role="img" aria-label="Data analytics illustration" style="background:linear-gradient(135deg,#16204a,#3e4fa0)"></div><div class="service-name">Data Analytics</div></div>
  <div class="service-card"><div class="service-img" role="img" aria-label="AI and machine learning illustration" style="background:linear-gradient(135deg,#0c2a56,#3fb2e8)"></div><div class="service-name">AI &amp; Machine Learning</div></div>
</section>

<div class="abs about-art" role="img" aria-label="Illustration: map of the continent drawn as a connected network"></div>
<section class="abs about-copy">
  <h2 class="about-title">About Us</h2>
  <p>Tavi Linkway Africa is a consultancy firm and digital marketplace dedicated to supporting Africa's digital transformation. We provide data-driven insights, strategic guidance, customised solutions to empower public and private sectors.</p>
  <p>We aim to tackle complex challenges, optimise operations, and unlock growth through innovative technology.</p>
  <p>Our marketplace offers a curated selection of digital products and tools designed to support strategic growth, expand knowledge, strengthen data capabilities, and streamline operations. With deep expertise in digital transformation and a focus on Africa's unique opportunities, Tavi Linkway Africa is your trusted partner in navigating today's dynamic digital landscape.</p>
  <p>Together, we're advancing Africa's digital future.</p>
</section>

<svg class="abs market-band" viewBox="0 0 1200 680" aria-hidden="true">
  <path d="M0 60 C220 10 420 110 640 70 C860 30 1000 0 1200 40 L1200 680 L0 680Z" fill="var(--mist)"/>
  <path d="M0 90 C240 40 440 140 660 100 C880 60 1020 40 1200 80 L1200 130 C1000 100 860 140 660 160 C420 190 220 110 0 150Z" fill="var(--cloud)"/>
</svg>

<h2 class="abs sec-title" style="top:1726px">Marketplace</h2>
<div class="abs tabs"><span>Templates</span><span>Guides</span><span class="on">Courses</span></div>

<section class="abs products">
  <article class="product">
    <div class="product-img" role="img" aria-label="Icon pack preview" style="background:linear-gradient(135deg,#fde2ea,#f7b7c9)"></div>
    <div class="product-body">
      <div class="product-head"><span class="product-name">SweetGlyphs</span><span class="price">$39 <small>Template</small></span></div>
      <p class="product-desc">A fresh icon set for apps and sites. Clean lines, easy to edit, made for fast and modern design work.</p>
      <div class="stars"><svg viewBox="0 0 20 20"><path d="M10 1l2.7 5.6 6.1.9-4.4 4.3 1 6.1L10 15l-5.4 2.9 1-6.1L1.2 7.5l6.1-.9z"/></svg><svg viewBox="0 0 20 20"><path d="M10 1l2.7 5.6 6.1.9-4.4 4.3 1 6.1L10 15l-5.4 2.9 1-6.1L1.2 7.5l6.1-.9z"/></svg><svg viewBox="0 0 20 20"><path d="M10 1l2.7 5.6 6.1.9-4.4 4.3 1 6.1L10 15l-5.4 2.9 1-6.1L1.2 7.5l6.1-.9z"/></svg><svg viewBox="0 0 20 20"><path d="M10 1l2.7 5.6 6.1.9-4.4 4.3 1 6.1L10 15l-5.4 2.9 1-6.1L1.2 7.5l6.1-.9z"/></svg><svg viewBox="0 0 20 20"><path d="M10 1l2.7 5.6 6.1.9-4.4 4.3 1 6.1L10 15l-5.4 2.9 1-6.1L1.2 7.5l6.1-.9z"/></svg>&nbsp;112 reviews</div>
      <a class="btn-shop">Shop Now</a><a class="btn-save">Saved Sample</a>
    </div>
  </article>
  <article class="product">
    <div class="product-img" role="img" aria-label="Spreadsheet template preview" style="background:linear-gradient(135deg,#d9f2dd,#8fd19c)"></div>
    <div class="product-body">
      <div class="product-head"><span class="product-name">TidyGrids</span><span class="price">$39 <small>Template</small></span></div>
      <p class="product-desc">Ready sheet kits for budgets and plans. Set up in minutes and keep your team data in order.</p>
      <div class="stars"><svg viewBox="0 0 20 20"><path d="M10 1l2.7 5.6 6.1.9-4.4 4.3 1 6.1L10 15l-5.4 2.9 1-6.1L1.2 7.5l6.1-.9z"/></svg><svg viewBox="0 0 20 20"><path d="M10 1l2.7 5.6 6.1.9-4.4 4.3 1 6.1L10 15l-5.4 2.9 1-6.1L1.2 7.5l6.1-.9z"/></svg><svg viewBox="0 0 20 20"><path d="M10 1l2.7 5.6 6.1.9-4.4 4.3 1 6.1L10 15l-5.4 2.9 1-6.1L1.2 7.5l6.1-.9z"/></svg><svg viewBox="0 0 20 20"><path d="M10 1l2.7 5.6 6.1.9-4.4 4.3 1 6.1L10 15l-5.4 2.9 1-6.1L1.2 7.5l6.1-.9z"/></svg><svg viewBox="0 0 20 20"><path d="M10 1l2.7 5.6 6.1.9-4.4 4.3 1 6.1L10 15l-5.4 2.9 1-6.1L1.2 7.5l6.1-.9z"/></svg>&nbsp;98 reviews</div>
      <a class="btn-shop">Shop Now</a><a class="btn-save">Saved Sample</a>
    </div>
  </article>
  <article class="product">
    <div class="product-img" role="img" aria-label="Course cover in purple and pink" style="background:linear-gradient(135deg,#7a3df0,#f0509a)"></div>
    <div class="product-body">
      <div class="product-head"><span class="product-name">Studio Course</span><span class="price">$39 <small>Course</small></span></div>
      <p class="product-desc">The Complete Studio Course. Learn to plan, price and grow a digital service step by step.</p>
      <div class="stars"><svg viewBox="0 0 20 20"><path d="M10 1l2.7 5.6 6.1.9-4.4 4.3 1 6.1L10 15l-5.4 2.9 1-6.1L1.2 7.5l6.1-.9z"/></svg><svg viewBox="0 0 20 20"><path d="M10 1l2.7 5.6 6.1.9-4.4 4.3 1 6.1L10 15l-5.4 2.9 1-6.1L1.2 7.5l6.1-.9z"/></svg><svg viewBox="0 0 20 20"><path d="M10 1l2.7 5.6 6.1.9-4.4 4.3 1 6.1L10 15l-5.4 2.9 1-6.1L1.2 7.5l6.1-.9z"/></svg><svg viewBox="0 0 20 20"><path d="M10 1l2.7 5.6 6.1.9-4.4 4.3 1 6.1L10 15l-5.4 2.9 1-6.1L1.2 7.5l6.1-.9z"/></svg><svg viewBox="0 0 20 20"><path d="M10 1l2.7 5.6 6.1.9-4.4 4.3 1 6.1L10 15l-5.4 2.9 1-6.1L1.2 7.5l6.1-.9z"/></svg>&nbsp;76 reviews</div>
      <a class="btn-shop">Shop Now</a><a class="btn-save">Saved Sample</a>
    </div>
  </article>
  <article class="product">
    <div class="product-img" role="img" aria-label="Icon set preview on blue cards" style="background:linear-gradient(135deg,#dfe9ff,#8fb0f2)"></div>
    <div class="product-body">
      <div class="product-head"><span class="product-name">SweetGlyphs</span><span class="price">$39 <small>Template</small></span></div>
      <p class="product-desc">A fresh icon set for apps and sites. Clean lines, easy to edit, made for fast and modern design work.</p>
      <div class="stars"><svg viewBox="0 0 20 20"><path d="M10 1l2.7 5.6 6.1.9-4.4 4.3 1 6.1L10 15l-5.4 2.9 1-6.1L1.2 7.5l6.1-.9z"/></svg><svg viewBox="0 0 20 20"><path d="M10 1l2.7 5.6 6.1.9-4.4 4.3 1 6.1L10 15l-5.4 2.9 1-6.1L1.2 7.5l6.1-.9z"/></svg><svg viewBox="0 0 20 20"><path d="M10 1l2.7 5.6 6.1.9-4.4 4.3 1 6.1L10 15l-5.4 2.9 1-6.1L1.2 7.5l6.1-.9z"/></svg><svg viewBox="0 0 20 20"><path d="M10 1l2.7 5.6 6.1.9-4.4 4.3 1 6.1L10 15l-5.4 2.9 1-6.1L1.2 7.5l6.1-.9z"/></svg><svg viewBox="0 0 20 20"><path d="M10 1l2.7 5.6 6.1.9-4.4 4.3 1 6.1L10 15l-5.4 2.9 1-6.1L1.2 7.5l6.1-.9z"/></svg>&nbsp;112 reviews</div>
      <a class="btn-shop">Shop Now</a><a class="btn-save">Saved Sample</a>
    </div>
  </article>
</section>

<h2 class="abs sec-title why-title" style="top:2272px">Why Choose Tavi Linkway <span>Africa?</span></h2>

<section class="abs reasons">
  <div class="reason">
    <div class="reason-icon"><svg viewBox="0 0 24 24" fill="none" stroke="#111" stroke-width="2"><circle cx="12" cy="12" r="9"/><circle cx="12" cy="12" r="5"/><circle cx="12" cy="12" r="1.5" fill="#111"/></svg></div>
    <h3>Tailored Solutions</h3>
    <p>Products and services designed for Africa's unique challenges.</p>
  </div>
  <div class="reason">
    <div class="reason-icon dark"><svg viewBox="0 0 24 24" fill="#fff"><circle cx="12" cy="8" r="4"/><path d="M4 21c0-4.4 3.6-7 8-7s8 2.6 8 7z"/></svg></div>
    <h3>Expert Guidance</h3>
    <p>Years of experience in digital transformation and innovation.</p>
  </div>
  <div class="reason">
    <div class="reason-icon"><svg viewBox="0 0 24 24" fill="none" stroke="#111" stroke-width="2" stroke-linecap="round" stroke-linejoin="round"><path d="M5 12l5 5L20 7"/></svg></div>
    <h3>Trustworthy Partner</h3>
    <p>Supporting both public and private sectors with actionable strategies.</p>
  </div>
</section>

<svg class="abs footer-bg" viewBox="0 0 1200 476" aria-hidden="true">
  <path d="M0 50 C260 0 480 100 720 60 C940 20 1060 10 1200 40 L1200 476 L0 476Z" fill="var(--night)"/>
</svg>

<section class="abs cta">
  <div>
    <h2>Let's Build Africa's Digital Future Together</h2>
    <p>Reach out to learn more about our services, marketplace products, or custom solutions.</p>
  </div>
  <a class="btn-dark">Shop Now</a>
</section>

<div class="abs f-brand">Tavi Linkway</div>
<div class="abs f-col" style="left:520px">
  <h4><span>Useful</span> Links</h4>
  <ul><li>Home</li><li>Services</li><li>Digital Marketplace</li><li>About Us</li><li>Blog</li><li>Contact</li></ul>
</div>
<div class="abs f-col" style="left:700px">
  <h4>Sign Up</h4>
  <p>Get our news and offers first. Make sure you don't miss any of our latest limited-time offers.</p>
  <div class="signup"><span>Email Address</span><b></b></div>
</div>
<div class="abs socials"><i></i><i></i><i></i><i></i><i></i></div>
<p class="abs copyright">© Copyright 2024 | All Rights Reserved</p>
<div class="abs to-top"></div>

</body>
</html>
```